Quillo Design Prize - $10,000 tablet app design contest, Event App Category

Quillo is a marketplace for Velo App Templates (similar to PageLoom templates). We want you to design an app template for sale in our marketplace which targets Event Apps (Velo Apps that are created around music festivals, tradeshows, conferences or other events).

It’s up to you to create pages or features for the App Template that you think are appropriate. Creativity will be rewarded! Here are some example pages or features that you could create:

• A welcome page
• Event details – when and where?
• A location map
• A contact details page
• An event calendar (what’s on when?)
• Social media integration
• Video or animations

Your design should be Vibrant, Engaging and Contemporary. If you have an Velo, download Quillo Viewer and download template examples in the download tab.

Your entry must include:
• A brief description of your template
• preview images of all pages of your template

Attached to this project are free templates to help you get started with your design. We have included:
1. A free portfolio template for designers/photographers
2. Icons and artwork to use in your template
3. Blank pages template
4. Form template
5. Video ad template

If you are selected as a finalist you will be required to submit an .oproject file containing:
• Your InDesign source files
• Preview images of your template
• All creative / stock assets used in the template (animations, video etc.)
• A text file with instructions on how to update the template
• A metadata .txt file containing template details and your information

How to enter:
1. Register at Marketplace and view the instructions under the welcome message https://marketplace.quillohub-example.com/welcome
2. Download Quillo Editor: https://support.quillohub-example.com/entries/58174096-quillo-editor
3. Use the free templates provided in this brief to create your designs and submit to Pencilyard

Reason: Due to the Christmas break we are extending the deadline of our competition. Thank you for time and effort - I will be providing feedback over the next couple of days! Best wishes, Loretta

Hi All,

I have received many screenshots with some great designs! I just wanted to clarify that you are designing Quillo app templates including Quillo features and not just page designs?

Read Tips for First Time Quilloers to guide you through the template creation process

Before you start designing templates for Quillo Marketplace

·       Read the Quality Standards

·       Read the Copyright Information 

·       Use the Template Quality Checklist to ensure your template follows our guidelines. 

What should my project file contain?

·       A folder containing your source files, e.g. InDesign. This must be named Source.

·       The Quillo content files. This must be named Bundle.

·       Instructions, explaining to a customer how to use your template.

Best wishes,

Loretta

Reason: We are extending the competition by 7 days to give you more time!

Reason: Hello - we have received 3 entries for this contest so we are extending the deadline by 7 days. Best wishes, Loretta :)

Target Market(s)

Entrepreneurs who wish to create Velo Apps by using our App design templates.

Industry/Entity Type

Events

Requirements
Must have
• You will need Quillo Editor to open the .oproject files attached to this brief. Get it here: https://support.quillohub-example.com/entries/58174096-quillo-editor
Should not have
• Low quality, fuzzy or blurry images
- Any stock images or content which you do not own the rights to
- Any material which could be considered inappropriate or offensive

```html
<!DOCTYPE html>
<html lang="en">
<head>
<meta charset="utf-8">
<title>Event App Template – Page Previews</title>
<link href="https://fonts.googleapis.com/css2?family=Barlow+Condensed:wght@500;600;700&family=Barlow+Semi+Condensed:wght@500;600;700&display=swap" rel="stylesheet">
<style>
  :root {
    --stage: #ffffff;
    --gutter: #101010;
    --brick: #de4f3d;
    --coral: #ef6b56;
    --lavender: #c6c5dd;
    --sky: #5ebfd9;
    --butter: #f6e6b0;
    --apricot: #e7b06a;
    --ink: #2a2a2a;
    --paper: #ffffff;
    --black: #0c0c0c;
    --rule: #e4b3a9;
    --head: "Barlow Condensed", "Arial Narrow", sans-serif;
    --body: "Barlow Semi Condensed", "Arial Narrow", sans-serif;
  }
  * { box-sizing: border-box; margin: 0; padding: 0; }
  html, body { width: 904px; height: 1200px; overflow: hidden; background: var(--gutter); }
  body { position: relative; font-family: var(--body); }
  .page { position: absolute; overflow: hidden; }
  .abs { position: absolute; }
  .head { font-family: var(--head); font-weight: 700; text-transform: uppercase; line-height: .88; }

  /* ---------- About page ---------- */
  .about { left: 0; top: 0; width: 446px; height: 590px; background: var(--brick); color: var(--paper); }
  .about .title { left: 42px; top: 14px; font-size: 82px; }
  .about .intro { left: 43px; top: 95px; width: 183px; font-family: var(--head); font-size: 10.6px; line-height: 13.6px; font-weight: 600; text-transform: uppercase; }
  .whats-on { left: 235px; top: 86px; font-size: 22px; }
  .whats-on-sub { left: 235px; top: 108px; width: 196px; font-family: var(--head); font-weight: 600; font-size: 14px; line-height: 15px; text-transform: uppercase; }
  .calendar { left: 235px; top: 157px; width: 194px; }
  .cal-head { display: flex; height: 47px; margin-bottom: 2px; }
  .cal-date { width: 78px; display: flex; align-items: center; justify-content: center; color: var(--black); font-weight: 700; font-size: 10.5px; }
  .cal-day { flex: 1; background: var(--coral); border: 1.5px solid var(--paper); display: flex; align-items: center; justify-content: center; font-weight: 600; font-size: 14px; }
  .cal-row { display: flex; height: 33px; border-bottom: 1px solid var(--rule); }
  .cal-time { width: 78px; background: var(--black); display: flex; align-items: center; justify-content: center; font-size: 12px; font-weight: 500; border-bottom: 1px solid #444; }
  .cal-event { flex: 1; background: var(--paper); color: var(--black); padding: 4px 5px; font-size: 11px; line-height: 11px; font-weight: 600; }
  .cal-event small { display: block; font-size: 8px; font-weight: 500; margin-top: 1px; }
  .cal-swipe { height: 10px; margin-top: 3px; background: repeating-linear-gradient(45deg, #3a3a3a 0 2px, #bbb 2px 4px); position: relative; }
  .cal-swipe span { position: absolute; right: 10px; top: 0; background: var(--paper); color: var(--black); font-size: 6px; font-weight: 700; padding: 1px 3px; line-height: 8px; }
  .featured { left: 43px; top: 309px; width: 180px; height: 178px; background: var(--paper); color: var(--coral); padding: 8px 5px; }
  .featured .name { font-size: 46px; line-height: 42px; font-weight: 600; }
  .featured .cta { margin-top: 8px; font-family: var(--head); font-weight: 600; font-size: 18.5px; line-height: 1; white-space: nowrap; text-transform: uppercase; }
  .where { left: 43px; top: 497px; font-size: 22px; }
  .where-addr { left: 43px; top: 520px; font-family: var(--head); font-weight: 600; font-size: 14px; line-height: 16px; }
  .where-addr b { font-weight: 600; text-transform: uppercase; }
  .where-rule { left: 262px; top: 528px; width: 106px; height: 1.5px; background: var(--paper); }
  .round-btn { border-radius: 50%; display: flex; align-items: center; justify-content: center; text-align: center; font-family: var(--head); font-weight: 600; text-transform: uppercase; line-height: 1; }
  .view-map { left: 369px; top: 499px; width: 60px; height: 60px; background: var(--paper); color: var(--black); font-size: 11px; }

  /* ---------- Contents page ---------- */
  .contents { left: 460px; top: 0; width: 444px; height: 590px; background: var(--stage); color: var(--ink); }
  .contents .title { left: 30px; top: 18px; font-size: 72px; }
  .nav-hint { left: 322px; top: 18px; width: 96px; text-align: center; font-size: 6.5px; line-height: 8px; font-weight: 600; }
  .nav-hint svg { display: block; margin: 0 auto 3px; }
  .tile { width: 143px; height: 143px; display: flex; flex-direction: column; align-items: center; justify-content: center; text-align: center; font-family: var(--head); font-weight: 700; text-transform: uppercase; line-height: .88; }
  .tile-about { left: 69px; top: 100px; background: var(--coral); color: var(--ink); font-size: 50px; }
  .tile-map { left: 69px; top: 253px; background: var(--sky); color: var(--ink); font-size: 72px; }
  .tile-bio { background: var(--lavender); color: var(--paper); }
  .tile-bio .big { font-size: 52px; }
  .tile-bio .small { font-size: 35px; font-weight: 600; margin-top: 4px; }
  .tile-bio2 { left: 222px; top: 100px; }
  .tile-bio1 { left: 69px; top: 407px; }
  .tile-feature { background: var(--butter); color: var(--ink); font-size: 44px; line-height: .8; }
  .tile-feature small { font-size: 16px; text-transform: none; margin-top: 6px; font-weight: 700; line-height: 1; }
  .tile-feat1 { left: 222px; top: 253px; }
  .tile-feat2 { left: 222px; top: 407px; }
  .next-arrow { left: 372px; top: 312px; }

  /* ---------- Social page ---------- */
  .social { left: 0; top: 600px; width: 446px; height: 600px; background: var(--apricot); color: var(--paper); }
  .social .title { left: 38px; top: 62px; font-size: 78px; display: flex; align-items: flex-end; gap: 12px; }
  .network { display: flex; align-items: center; gap: 5px; font-family: var(--head); font-weight: 700; font-size: 20px; text-transform: none; line-height: 1; padding-bottom: 8px; }
  .network i { display: block; width: 12px; height: 12px; border-radius: 50%; background: var(--paper); }
  .to-contents { left: 360px; top: 66px; width: 54px; height: 54px; background: var(--coral); color: var(--paper); font-size: 11px; }
  .hashtag { left: 40px; top: 158px; font-family: var(--head); font-weight: 600; font-size: 18px; }
  .feed { left: 40px; top: 183px; width: 190px; height: 300px; border: 1px dashed var(--paper); padding: 4px; }
  .feed-inner { width: 100%; height: 100%; background: var(--paper); color: var(--black); font-size: 8px; line-height: 9.5px; padding: 6px 8px; font-weight: 500; }
  .feed-inner p { border-bottom: 1px solid #ddd; padding-bottom: 6px; }
  .have-say { left: 41px; top: 498px; width: 188px; height: 24px; background: var(--coral); display: flex; align-items: center; justify-content: center; font-family: var(--head); font-weight: 600; font-size: 16px; text-transform: uppercase; }
  .social-quote { left: 241px; top: 198px; width: 178px; font-size: 10.4px; line-height: 13.6px; font-weight: 600; }
  .contact-card { left: 241px; top: 314px; width: 174px; height: 172px; background: var(--paper); color: var(--coral); text-align: center; padding-top: 16px; font-family: var(--head); font-weight: 600; text-transform: uppercase; }
  .contact-card .kicker { font-size: 12.5px; }
  .contact-card .big { font-size: 33px; line-height: 33px; margin: 14px 0 12px; }

  /* ---------- Event detail page ---------- */
  .detail { left: 460px; top: 600px; width: 444px; height: 600px; background: var(--stage); color: var(--ink); }
  .detail .title { left: 30px; top: -62px; font-size: 78px; color: var(--sky); }
  .copy { font-size: 9.4px; line-height: 13.4px; font-weight: 600; }
  .copy p + p { margin-top: 13px; }
  .col-left { left: 30px; top: 24px; width: 184px; }
  .gallery { left: 222px; top: 24px; width: 198px; height: 224px; background: var(--lavender); display: flex; align-items: center; justify-content: center; font-family: var(--head); font-weight: 600; font-size: 22px; color: var(--ink); }
  .gallery-hint { left: 222px; top: 252px; font-size: 7px; color: var(--lavender); font-weight: 600; }
  .label { font-family: var(--head); font-weight: 600; font-size: 15px; text-transform: uppercase; }
  .time-label { left: 222px; top: 292px; color: var(--coral); }
  .time-val { left: 222px; top: 314px; color: var(--coral); font-family: var(--head); font-weight: 600; font-size: 12px; }
  .view-cal { left: 361px; top: 282px; width: 60px; height: 60px; background: var(--coral); color: var(--paper); font-size: 11px; }
  .loc-label { left: 222px; top: 350px; color: var(--sky); }
  .loc-val { left: 222px; top: 372px; color: var(--sky); font-family: var(--head); font-weight: 600; font-size: 12px; }
  .map-btn { left: 222px; top: 395px; width: 198px; height: 52px; background: var(--sky); color: var(--paper); display: flex; align-items: center; justify-content: center; font-family: var(--head); font-weight: 600; font-size: 21px; }
  .col-full { left: 30px; top: 466px; width: 390px; }
  .pull-quote { left: 36px; top: 560px; color: var(--sky); font-family: var(--head); font-weight: 600; font-size: 15px; }
  .col-right { left: 222px; top: 562px; width: 198px; }
</style>
</head>
<body>

<!-- About -->
<section class="page about">
  <h1 class="abs head title">About</h1>
  <p class="abs intro">Aliquam erat volutpat. Proin molestie neque nec quam tempus condimentum. Morbi pretium ligula a elit blandit vulputate. Nullam lacinia urna et felis sollicitudin et pulvinar nisi vestibulum. Lorem ipsum dolor sit amet, consectetur adipiscing elit. Integer justo neque, malesuada ut semper id, laoreet sit amet enim. Vivamus mauris magna, pharetra vitae pharetra eget, vulputate at quam. Morbi vestibulum posuere feugiat. Curabitur sit amet sem lorem. Phasellus ullamcorper sem et diam viverra ultricies. Integer sit amet nibh ac urna vestibulum rutrum. Phasellus fermentum, massa eu pellentesque quis.</p>

  <h2 class="abs head whats-on">What’s on?</h2>
  <p class="abs whats-on-sub">Swipe the calendar to view each day’s events.</p>

  <div class="abs calendar">
    <div class="cal-head"><div class="cal-date">01/01/2013</div><div class="cal-day">Monday</div></div>
    <div class="cal-row"><div class="cal-time">9am</div><div class="cal-event">Event<small>(Tap to save in calendar)</small></div></div>
    <div class="cal-row"><div class="cal-time">10am</div><div class="cal-event">Event<small>(Tap to save in calendar)</small></div></div>
    <div class="cal-row"><div class="cal-time">11am</div><div class="cal-event">Event<small>(Tap to save in calendar)</small></div></div>
    <div class="cal-row"><div class="cal-time">12pm</div><div class="cal-event">Event<small>(Tap to save in calendar)</small></div></div>
    <div class="cal-row"><div class="cal-time">1pm</div><div class="cal-event">Event<small>(Tap to save in calendar)</small></div></div>
    <div class="cal-row"><div class="cal-time">2pm</div><div class="cal-event">Event<small>(Tap to save in calendar)</small></div></div>
    <div class="cal-row"><div class="cal-time">3pm</div><div class="cal-event">Event<small>(Tap to save in calendar)</small></div></div>
    <div class="cal-row"><div class="cal-time">4pm</div><div class="cal-event">Event<small>(Tap to save in calendar)</small></div></div>
    <div class="cal-swipe"><span>SWIPE TO VIEW MORE</span></div>
  </div>

  <div class="abs featured">
    <div class="head name">Featured<br>Item<br>Name</div>
    <div class="cta">Tap to view full list</div>
  </div>

  <h2 class="abs head where">Where?</h2>
  <p class="abs where-addr"><b>The Suchandsuch Convention Centre.</b><br>1 Here-or-there Rd, Somewhere.</p>
  <div class="abs where-rule"></div>
  <div class="abs round-btn view-map">View<br>Map</div>
</section>

<!-- Contents -->
<section class="page contents">
  <h1 class="abs head title">Contents</h1>
  <div class="abs nav-hint">
    <svg width="40" height="16" viewBox="0 0 40 16" aria-hidden="true">
      <path d="M3 4h10M3 4l3-2M13 4l-3-2" stroke="#2a2a2a" stroke-width="1.2" fill="none"/>
      <rect x="6" y="6" width="3" height="9" rx="1.5" fill="#2a2a2a"/>
      <circle cx="30" cy="4" r="3" fill="none" stroke="#2a2a2a" stroke-width="1.2"/>
      <rect x="28.5" y="5" width="3" height="10" rx="1.5" fill="#2a2a2a"/>
    </svg>
    Navigate pages by swiping between them. Tap an item to view it.
  </div>

  <div class="abs tile tile-about">About</div>
  <div class="abs tile tile-bio tile-bio2"><span class="big">Bio#2:</span><span class="small">Person’s<br>Name</span></div>
  <div class="abs tile tile-map">Map</div>
  <div class="abs tile tile-feature tile-feat1">Feature<br>Event<br>Name 1<small>Sub-Title.</small></div>
  <div class="abs tile tile-bio tile-bio1"><span class="big">Bio#1:</span><span class="small">Person’s<br>Name</span></div>
  <div class="abs tile tile-feature tile-feat2">Feature<br>Event<br>Name 2<small>Sub-Title.</small></div>

  <svg class="abs next-arrow" width="14" height="26" viewBox="0 0 14 26" aria-hidden="true"><path d="M0 0L14 13L0 26Z" fill="#2a2a2a"/></svg>
</section>

<!-- Social -->
<section class="page social">
  <h1 class="abs head title">Tweet <span class="network"><i></i>Chirpline</span></h1>
  <div class="abs round-btn to-contents">Contents<br>Page</div>
  <p class="abs hashtag">#YourTweetName</p>
  <div class="abs feed"><div class="feed-inner"><p>No tweets found at the moment for "#YourTweetName".</p></div></div>
  <div class="abs have-say">Have your say!</div>
  <p class="abs social-quote">“Aenean diam mi, volutpat eu dictum id, fermentum eu lacus. Donec arcu arcu, sollicitudin nec consequat eget, fermentum non neque. Vestibulum ante ipsum primis in faucibus orci luctus et ultrices posuere cubilia Curae; Sed nec ante ligula. Nulla facilisi. Mauris a arcu leo. Nunc a velit augue, a gravida mi.”</p>
  <div class="abs contact-card">
    <div class="kicker">Check out our</div>
    <div class="big">Contact<br>Page</div>
    <div class="kicker">For more connections</div>
  </div>
</section>

<!-- Event detail -->
<section class="page detail">
  <h1 class="abs head title">Title #1</h1>
  <div class="abs copy col-left">
    <p>Lorem ipsum dolor sit amet, consectetur adipiscing elit. Pellentesque in est vel diam faucibus eleifend nec nec felis. Proin fringilla ullamcorper facilisis. Pellentesque eu nisi et sem mollis luctus. Vestibulum sit amet tellus et arcu pretium lobortis. Nam varius, odio eget gravida porttitor, augue est congue justo, eget interdum eros justo sit amet lectus. Pellentesque eros ante, dictum eget commodo nec, eleifend at dui. Nam lobortis, purus et auctor euismod, metus nisl iaculis lacus, in scelerisque ipsum ipsum at turpis. Morbi cursus luctus mauris a condimentum. Nunc feugiat magna eget dui tincidunt vitae laoreet dolor viverra. Nullam gravida nisi non purus dictum dapibus. Cum sociis natoque penatibus et magnis dis parturient montes, nascetur ridiculus mus. Pellentesque facilisis tincidunt dictum. Etiam vulputate semper eros at cursus. Nullam adipiscing erat aliquam massa aliquam sed mollis nisi congue.</p>
    <p>Aenean diam mi, volutpat eu dictum id, fermentum eu lacus. Donec arcu arcu, sollicitudin nec consequat eget, fermentum non neque. Vestibulum ante ipsum primis in faucibus orci luctus et ultrices posuere cubilia Curae; Sed nec ante ligula. Nulla facilisi. Mauris a arcu leo. Nunc a velit augue, a gravida mi. Lorem ipsum dolor sit amet, consectetur adipiscing elit. Donec id tellus libero, ac varius augue. Aenean ultrices, ligula commodo tempor auctor, arcu turpis ultricies massa, quis adipiscing nibh est sit amet ligula.</p>
  </div>
  <div class="abs gallery" role="img" aria-label="Event image gallery placeholder">IMAGE 1</div>
  <p class="abs gallery-hint">Swipe to view images.</p>
  <p class="abs label time-label">Time:</p>
  <p class="abs time-val">1PM, Monday 01/01/13</p>
  <div class="abs round-btn view-cal">View<br>Calendar</div>
  <p class="abs label loc-label">Location:</p>
  <p class="abs loc-val">1 Here-or-there Rd, Somewhere.</p>
  <div class="abs map-btn">Show on Map</div>
  <div class="abs copy col-full"><p>Mauris tincidunt arcu in leo eleifend adipiscing. Duis eget eros libero. Praesent lacinia sollicitudin nunc et ultricies. Mauris viverra elit eget mauris pulvinar interdum tincidunt risus venenatis. Aenean mattis imperdiet sodales. Duis euismod nulla vitae nunc fermentum egestas. Donec scelerisque purus in turpis fringilla pharetra. Curabitur tempor rhoncus purus. Pellentesque eu ligula sed tellus pretium blandit eu et neque. Sed pharetra porta rutrum. Pellentesque habitant morbi tristique senectus et netus et malesuada fames ac turpis egestas. Vivamus euismod nulla ut lectus faucibus in egestas quam malesuada.</p></div>
  <p class="abs pull-quote">“Aenean diam mi, volutpat</p>
  <div class="abs copy col-right"><p>Aliquam posuere imperdiet elit, quis fringilla odio ornare quis. Cras gravida, nisl vitae fringilla fermentum, eros augue suscipit nulla, at tempor nibh magna eu diam.</p></div>
</section>

</body>
</html>
```